A5 front cover for a programme DANCE

To design a front cover for our dance Academy 15th Year anniversary show. The theme is movies and musicals

the school is called Bramblewick Academy of Dance and Performing Arts

venue Harcliffe Playhouse

a5 fornt cover
date 30th June 2019

show title Hold the chorus

Number of Pages Required

1 page

Font styles to use
Sans Serif

Colors

Designer to choose colors to be used in the design.

Requirements
Must have
• up to date fun

```html
<!DOCTYPE html>
<html lang="en">
<head>
<meta charset="utf-8">
<title>Hold the Chorus – 15th Anniversary Show Programme Cover</title>
<link rel="stylesheet" href="https://fonts.googleapis.com/css2?family=Lobster&family=Poppins:wght@800&family=Bungee&family=Hind:wght@400&display=swap">
<style>
  :root {
    --page-bg: #ececec;
    --crimson: #d3141f;
    --wine: #8c1240;
    --plum: #4d0f3d;
    --deep-plum: #3a0b30;
    --title-ink: #4a0a3a;
    --glow-pink: #f59ee0;
    --soft-pink: #f4b8ec;
    --lavender: #f7c9f2;
    --white: #ffffff;
    --logo-ink: #1c0610;
  }
  * { margin: 0; padding: 0; box-sizing: border-box; }
  html, body {
    width: 1200px; height: 1200px; overflow: hidden;
    background: var(--page-bg);
  }
  .cover {
    position: absolute; left: 194px; top: 25px;
    width: 811px; height: 1150px; overflow: hidden;
    box-shadow: 0 4px 14px rgba(0,0,0,0.25);
  }
  .cover__photo {
    position: absolute; inset: 0;
    background:
      radial-gradient(ellipse at 70% 55%, rgba(240,30,50,0.85) 0%, rgba(240,30,50,0) 45%),
      radial-gradient(ellipse at 15% 78%, rgba(215,20,30,0.9) 0%, rgba(215,20,30,0) 50%),
      linear-gradient(160deg, var(--wine) 0%, var(--plum) 30%, var(--crimson) 60%, var(--deep-plum) 100%);
  }
  .cover__diamond { position: absolute; inset: 0; }
  .cover > .text { position: absolute; left: 0; width: 100%; text-align: center; }
  .show-title {
    top: 40px; font-family: "Lobster", cursive; font-size: 74px;
    color: var(--title-ink); line-height: 1;
    -webkit-text-stroke: 2px var(--glow-pink);
    text-shadow: 0 0 12px rgba(245,158,224,0.8);
  }
  .anniversary-number {
    top: 222px; font-family: "Poppins", sans-serif; font-weight: 800;
    font-size: 200px; line-height: 1; letter-spacing: -6px;
    background: linear-gradient(180deg, #fde8fb 0%, #f08ee0 100%);
    -webkit-background-clip: text; background-clip: text; color: transparent;
    filter: drop-shadow(0 0 10px rgba(245,158,224,0.7));
  }
  .anniversary-number sup { font-size: 100px; vertical-align: 72px; letter-spacing: 0; }
  .anniversary-word {
    top: 432px; font-family: "Bungee", sans-serif; font-size: 54px;
    color: var(--white); line-height: 1;
  }
  .show-word {
    top: 498px; font-family: "Lobster", cursive; font-size: 62px;
    color: var(--white); line-height: 1;
  }
  .academy-name {
    top: 562px; font-family: "Hind", sans-serif; font-size: 28px;
    color: var(--white); line-height: 40px; letter-spacing: 1px;
    padding: 0 110px;
  }
  .rule {
    position: absolute; left: 210px; width: 352px; height: 3px;
    background: linear-gradient(90deg, rgba(255,220,240,0), #ffd6ef 20%, #ffd6ef 80%, rgba(255,220,240,0));
  }
  .rule--top { top: 654px; }
  .rule--bottom { top: 748px; }
  .show-date {
    top: 664px; font-family: "Hind", sans-serif; font-size: 64px;
    color: var(--soft-pink); line-height: 80px; word-spacing: 10px;
  }
  .show-date sup { font-size: 32px; vertical-align: 28px; }
  .show-date .month { color: var(--lavender); }
  .academy-mark {
    top: 806px; font-family: "Hind", sans-serif; font-size: 40px;
    color: var(--logo-ink); line-height: 50px;
    display: flex; justify-content: center; align-items: center; gap: 10px;
  }
  .academy-mark__dot {
    width: 20px; height: 20px; border-radius: 50%; background: var(--logo-ink);
  }
  .venue {
    top: 1068px; font-family: "Hind", sans-serif; font-size: 38px;
    color: var(--white); line-height: 46px; word-spacing: 6px;
  }
  .venue__label { color: var(--soft-pink); }
  .venue__divider {
    display: inline-block; width: 2px; height: 46px; background: var(--white);
    vertical-align: -8px; margin: 0 10px;
  }
</style>
</head>
<body>
  <main class="cover">
    <div class="cover__photo" role="img" aria-label="Photo of a ballroom dance couple in red costume above a cheering concert crowd, bathed in red and purple stage light"></div>
    <svg class="cover__diamond" width="811" height="1150" viewBox="0 0 811 1150" aria-hidden="true">
      <polygon points="398,46 718,553 398,1070 78,553" fill="rgba(255,180,230,0.06)" stroke="rgba(255,190,235,0.35)" stroke-width="10"/>
    </svg>

    <h1 class="text show-title">Hold the Chorus</h1>
    <div class="text anniversary-number">15<sup>th</sup></div>
    <div class="text anniversary-word">ANNIVERSARY</div>
    <div class="text show-word">Show</div>
    <p class="text academy-name">BRAMBLEWICK ACADEMY OF DANCE AND PERFORMING ARTS</p>

    <div class="rule rule--top"></div>
    <p class="text show-date">30<sup>th</sup> <span class="month">JUNE</span> 2019</p>
    <div class="rule rule--bottom"></div>

    <div class="text academy-mark"><span class="academy-mark__dot"></span><span>Bramblewick</span></div>

    <p class="text venue"><span class="venue__label">VENUE</span><span class="venue__divider"></span>HARCLIFFE PLAYHOUSE</p>
  </main>
</body>
</html>
```